Executive Business Consulting for Telco Companies and Telco Start up companies

1.) Looking for an appealing and action oriented business card design.
2.)The target companies to work with start-ups and existing companies that focus on Business to Business applications
3.) For "OKRA", a Belgium based Executive consultancy company specialised in global reach starting from the centre of Europe = Brussels.
4.) Our core competence is the Go To Market in All major global regions, incl North America, Latin America, Asia, Japan, Europe and Africa.
5.) Design should be appealing to CEO, CFO and Venture Funds signalling; Expertise, Stability, Maturity and Commitment
6.) Preferred color scheme is Blue focussed and using a modern FONT.
7.) Logo design is included (uploaded)

Target Market(s)

Telecommunication Market. Companies in a B2B business model, developping services or applications to make business run more profitable

Industry/Entity Type

Business

Contact Information for Business Card

Company Name: OKRA
Name: Joris Vandelay
Titel: Managing Director
Address: Kalkweg 58 , B-9170 Meerdonk , Belgium
Tel: + 32 471 208 364
Email: joris_vandelay@plimbox.example
LinkedIn: be.netprofilo.example/in/jorisvandelay/

Font styles to use
Serif

Colors
0455a3
3277b5

Requirements
Must have
• Second Side Text: Execute Sales Strategy and Transformation

```html
<!DOCTYPE html>
<html lang="en">
<head>
<meta charset="utf-8">
<title>OKRA – Business Card</title>
<link href="https://fonts.googleapis.com/css2?family=Noto+Serif:ital,wght@0,400;0,700;1,400&display=swap" rel="stylesheet">
<style>
  :root {
    --blue-deep: #0455a3;
    --blue-mid: #3277b5;
    --blue-dark: #033d78;
    --navy: #12306a;
    --white: #ffffff;
    --paper: #f4f5f7;
    --edge-grey: #b7bbc3;
    --stage: #e6e8ec;
  }
  html, body {
    margin: 0;
    padding: 0;
    overflow: hidden;
  }
  body {
    width: 1200px;
    height: 900px;
    background: var(--stage);
    font-family: "Noto Serif", serif;
    display: flex;
    align-items: center;
    justify-content: center;
    gap: 60px;
  }
  .card {
    position: relative;
    width: 520px;
    height: 310px;
    border-radius: 30px;
    overflow: hidden;
    box-shadow: 0 10px 28px rgba(20, 40, 80, 0.18);
  }

  /* Front side */
  .card--front {
    background: radial-gradient(circle at 30% 35%, var(--blue-mid) 0%, var(--blue-deep) 55%, var(--blue-dark) 100%);
  }
  .front__panel {
    position: absolute;
    left: 240px;
    top: 0;
    right: 0;
    bottom: 0;
    background: linear-gradient(160deg, var(--white) 0%, var(--paper) 100%);
    border-top-left-radius: 150px 170px;
    box-shadow: -9px 0 0 var(--edge-grey);
  }
  .front__identity {
    position: absolute;
    left: 130px;
    top: 16px;
    color: var(--white);
  }
  .front__name {
    margin: 0;
    font-size: 15px;
    font-weight: 400;
    font-style: italic;
  }
  .front__title {
    margin: 2px 0 0;
    font-size: 11px;
    font-weight: 400;
    opacity: 0.9;
  }
  .front__contacts {
    position: absolute;
    left: 18px;
    top: 132px;
    margin: 0;
    padding: 0;
    list-style: none;
    color: var(--white);
    font-size: 10.5px;
  }
  .front__contacts li {
    display: flex;
    align-items: center;
    gap: 7px;
    height: 18px;
    white-space: nowrap;
  }
  .contact-icon {
    width: 12px;
    height: 12px;
    flex: none;
  }
  .front__brand {
    position: absolute;
    left: 262px;
    top: 120px;
    right: 14px;
    display: flex;
    align-items: center;
    justify-content: center;
    gap: 12px;
  }
  .brand-name {
    font-size: 50px;
    font-weight: 700;
    letter-spacing: 1px;
    color: var(--navy);
    line-height: 1;
  }
  .brand-dot {
    width: 34px;
    height: 34px;
    border-radius: 50%;
    background: var(--blue-deep);
    flex: none;
  }

  /* Back side */
  .card--back {
    background: linear-gradient(160deg, var(--white) 0%, var(--paper) 100%);
    display: flex;
    flex-direction: column;
    align-items: center;
    justify-content: center;
    gap: 22px;
  }
  .back__brand {
    display: flex;
    align-items: center;
    gap: 16px;
  }
  .card--back .brand-name {
    font-size: 60px;
  }
  .back__tagline {
    margin: 0;
    font-size: 15px;
    font-style: italic;
    color: var(--blue-deep);
    letter-spacing: 0.3px;
  }
</style>
</head>
<body>

  <section class="card card--front" aria-label="Business card front">
    <div class="front__panel"></div>

    <div class="front__identity">
      <p class="front__name">Joris Vandelay</p>
      <p class="front__title">Managing Director</p>
    </div>

    <ul class="front__contacts">
      <li>
        <svg class="contact-icon" viewBox="0 0 12 12" aria-hidden="true">
          <circle cx="6" cy="6" r="6" fill="#ffffff"/>
          <path d="M4 3.2l1 1-0.6 0.9c0.4 0.8 1 1.4 1.8 1.8l0.9-0.6 1 1-0.7 1C5.6 8.2 3.8 6.4 3.1 4.1z" fill="#0455a3"/>
        </svg>
        + 32 471 208 364
      </li>
      <li>
        <svg class="contact-icon" viewBox="0 0 12 12" aria-hidden="true">
          <circle cx="6" cy="6" r="6" fill="#ffffff"/>
          <rect x="4.2" y="2.8" width="3.6" height="6.4" rx="0.7" fill="#0455a3"/>
          <rect x="4.9" y="3.6" width="2.2" height="3.9" fill="#ffffff"/>
        </svg>
        + 32 471 208 364
      </li>
      <li>
        <svg class="contact-icon" viewBox="0 0 12 12" aria-hidden="true">
          <circle cx="6" cy="6" r="6" fill="#ffffff"/>
          <rect x="3" y="4" width="6" height="4.2" fill="#0455a3"/>
          <path d="M3 4l3 2.3L9 4" fill="none" stroke="#ffffff" stroke-width="0.7"/>
        </svg>
        joris_vandelay@plimbox.example
      </li>
    </ul>

    <div class="front__brand">
      <span class="brand-name">OKRA</span>
      <span class="brand-dot" aria-hidden="true"></span>
    </div>
  </section>

  <section class="card card--back" aria-label="Business card back">
    <div class="back__brand">
      <span class="brand-dot" aria-hidden="true"></span>
      <span class="brand-name">OKRA</span>
    </div>
    <p class="back__tagline">Execute Sales Strategy and Transformation</p>
  </section>

</body>
</html>
```